Specialised investor in e-mobility and energy wants business card design

We need a business card design that fits our existing corporate design. <The look and feel must be 'sharp'/'clean', dynamic, communicate momentum, professionalism etc (as one would imagine from a firm in the financial sector). We like the idea of a reverse-side of the card that includes the logo, and the name and contact details on the other. We expect the deliverable to be whatever format might be required to be able to get cards printed directly by a service such as marlo cards. Our website is www.obrel.finance

```html
<!DOCTYPE html>
<html lang="en">
<head>
<meta charset="utf-8">
<title>Obrel Capital – Business Card</title>
<link rel="stylesheet" href="https://fonts.googleapis.com/css2?family=Arimo:wght@400;700&display=swap">
<style>
  :root {
    --backdrop: #2d2d2d;
    --card: #000000;
    --accent: #86b94a;
    --brand-dark: #3b5e2b;
    --text-light: #ffffff;
  }
  * { margin: 0; padding: 0; box-sizing: border-box; }
  html, body {
    width: 1200px;
    height: 1015px;
    overflow: hidden;
    background: var(--backdrop);
    font-family: "Arimo", Arial, sans-serif;
  }
  .sheet {
    width: 1200px;
    height: 1015px;
    display: flex;
    flex-direction: column;
    align-items: center;
    justify-content: center;
    gap: 64px;
  }
  .card {
    position: relative;
    width: 588px;
    height: 336px;
    background: var(--card);
    box-shadow: 0 14px 30px rgba(0, 0, 0, 0.45);
    overflow: hidden;
  }
  .card__band {
    position: absolute;
    left: 0;
    right: 0;
    bottom: 0;
    height: 9px;
    background: var(--accent);
  }
  .brand {
    display: flex;
    align-items: center;
    gap: 12px;
    color: var(--brand-dark);
    font-weight: 400;
    white-space: nowrap;
  }
  .brand__mark {
    width: 16px;
    height: 16px;
    background: var(--brand-dark);
  }
  .card--back .brand {
    position: absolute;
    left: 50%;
    top: 50%;
    transform: translate(-50%, -58%);
    font-size: 52px;
  }
  .card--front .brand {
    position: absolute;
    right: 34px;
    top: 70px;
    font-size: 34px;
    gap: 9px;
  }
  .card--front .brand__mark { width: 11px; height: 11px; }
  .contact {
    position: absolute;
    left: 44px;
    top: 118px;
    color: var(--text-light);
  }
  .contact__name {
    color: var(--accent);
    font-weight: 700;
    font-size: 19px;
    letter-spacing: 0.3px;
  }
  .contact__role {
    font-size: 13px;
    letter-spacing: 0.4px;
    margin-top: 2px;
  }
  .contact__rule {
    width: 110px;
    height: 1px;
    background: var(--accent);
    margin: 16px 0 14px 30px;
  }
  .contact__list { list-style: none; font-size: 14px; line-height: 19px; }
  .contact__list li { display: flex; align-items: center; gap: 8px; padding-left: 14px; }
  .contact__icon { width: 12px; height: 12px; flex: none; }
  .contact__address { font-size: 14px; line-height: 19px; padding-left: 44px; }
</style>
</head>
<body>
<main class="sheet">
  <section class="card card--back" aria-label="Card back">
    <div class="brand"><span class="brand__mark"></span><span class="brand__name">Obrel Capital</span></div>
    <div class="card__band"></div>
  </section>

  <section class="card card--front" aria-label="Card front">
    <div class="brand"><span class="brand__mark"></span><span class="brand__name">Obrel Capital</span></div>
    <div class="contact">
      <p class="contact__name">JONATHAN SMITH</p>
      <p class="contact__role">MANAGING DIRECTOR</p>
      <div class="contact__rule"></div>
      <ul class="contact__list">
        <li>
          <svg class="contact__icon" viewBox="0 0 12 12"><path d="M2.5 1 L4.5 3.4 L3.4 4.6 Q4.6 7.2 7.4 8.6 L8.6 7.5 L11 9.5 L9.6 11 Q4.5 10.5 1 2.4 Z" fill="var(--accent)"/></svg>
          <span>044-123 456 789</span>
        </li>
        <li>
          <svg class="contact__icon" viewBox="0 0 12 12"><rect x="0.5" y="2" width="11" height="8" fill="var(--accent)"/><path d="M0.5 2 L6 6.6 L11.5 2" fill="none" stroke="#000" stroke-width="1"/></svg>
          <span>info@webname.com</span>
        </li>
        <li>
          <svg class="contact__icon" viewBox="0 0 12 12" fill="none" stroke="var(--accent)" stroke-width="1.1"><circle cx="6" cy="6" r="5"/><ellipse cx="6" cy="6" rx="2.2" ry="5"/><path d="M1 6 H11 M2 3.5 H10 M2 8.5 H10"/></svg>
          <span>www.websitename.com</span>
        </li>
      </ul>
      <div class="contact__rule"></div>
      <p class="contact__address">421, Address line goes here<br>45452,Country Name</p>
    </div>
    <div class="card__band"></div>
  </section>
</main>
</body>
</html>
```